Commercial and Residential Paint Contractor needs website

We need a website for our residential painting, multi-family painting and commercial painting company. We paint interior and exterior of houses, apartments and commercial buildings. I would like an about us page, residential page, multi family page, commercial page and contact us. Need keywords added to website for seo opitimazation. I like this website https://www.velmorandhalestudio.com/

Target Market(s)

General Contractors and commercial property managers

Coding

Coded - Design and coding required

Number of Pages Required

5+ page

Font styles to use
Sans Serif

Requirements
Must have
• I need SEO keywords on pages

```html
<!DOCTYPE html>
<html lang="en">
<head>
<meta charset="utf-8">
<title>Hartwell Painting — Residential, Multi-Family &amp; Commercial Painting</title>
<meta name="description" content="Hartwell Painting: residential painting, commercial painting and multi-family painting contractor for interior and exterior projects.">
<link rel="stylesheet" href="https://fonts.googleapis.com/css2?family=Open+Sans:ital,wght@0,400;0,600;0,700;0,800;1,700;1,800&display=swap">
<style>
:root{
  --navy:#0b4a96;
  --brand:#12468f;
  --red:#e0161e;
  --ink:#2b2b2b;
  --muted:#4a4a4a;
  --light:#eef5fc;
  --band:#5a88b8;
  --footer:#0b2a4e;
  --footer-deep:#09223f;
  --white:#ffffff;
}
*{box-sizing:border-box;margin:0;padding:0}
html,body{width:1200px;height:4177px;overflow:hidden;background:var(--white)}
body{font-family:"Open Sans",sans-serif;color:var(--ink)}
.page{position:relative;width:1200px;height:4177px;overflow:hidden}
.abs{position:absolute}
.photo{position:absolute;z-index:0}
.btn{position:absolute;background:var(--red);color:var(--white);font-weight:700;font-size:16px;display:flex;align-items:center;justify-content:center;border-radius:3px;transform:skewX(-3deg);z-index:2}
.title{position:absolute;color:var(--brand);font-weight:600;font-size:33px;line-height:1;z-index:2}
.rule{position:absolute;height:4px;background:var(--red);border-radius:2px;z-index:2}
.center{left:0;width:1200px;text-align:center}
.rule.center-rule{left:555px;width:90px}
p.body{font-size:15.5px;line-height:19px;color:var(--muted);text-align:justify;z-index:2}

/* header */
.header{position:absolute;left:0;top:0;width:1200px;height:83px;background:var(--white)}
.brand{position:absolute;left:89px;top:28px;display:flex;align-items:center;gap:10px;font-weight:800;font-size:30px;color:var(--brand);letter-spacing:.5px}
.brand-dot{width:14px;height:14px;background:var(--red)}
.nav a{position:absolute;top:43px;font-size:15px;font-weight:600;color:#111;text-decoration:none}
.nav .active{color:var(--red)}
.nav .active::after{content:"";position:absolute;left:-4px;right:-4px;bottom:-8px;height:3px;background:var(--navy)}
.nav .contact-btn{top:34px;left:1002px;width:110px;height:36px;background:var(--red);color:var(--white);display:flex;align-items:center;justify-content:center;border-radius:2px}

/* hero */
.hero{position:absolute;left:0;top:83px;width:1200px;height:680px;background:linear-gradient(180deg,#0a4a9c,#0b4790)}
.hero-kicker{position:absolute;left:211px;top:162px;color:var(--white);font-size:39px;font-weight:400;z-index:2}
.hero-word{position:absolute;left:198px;top:212px;color:var(--red);font-size:116px;line-height:1.1;font-weight:800;font-style:italic;letter-spacing:-3px;text-shadow:0 6px 8px rgba(0,0,0,.35);z-index:2;white-space:nowrap}
.hero-stroke{position:absolute;left:208px;top:455px;width:250px;height:24px;background:linear-gradient(90deg,rgba(200,210,225,.4),rgba(200,210,225,.85),rgba(200,210,225,.3));border-radius:12px;z-index:2}
.arrow-ring{position:absolute;width:62px;height:62px;border:3px solid rgba(255,255,255,.8);border-radius:50%;z-index:2}
.dots{position:absolute;display:flex;gap:14px;z-index:2}
.dots span{width:10px;height:10px;border-radius:50%;background:#5f7fb0}
.dots span.on{background:var(--red)}
.svc-dots span{background:#8fb1d8}
.svc-dots span.on{background:var(--navy)}

/* services */
.services-bg{position:absolute;left:0;top:1249px;width:1200px;height:800px;background:var(--light)}
.svc-circle{position:absolute;width:254px;height:254px;border-radius:50%}
.svc-name{position:absolute;width:300px;text-align:center;color:var(--brand);font-size:21px;font-weight:600}
.svc-text{position:absolute;width:256px}

/* why */
.bullets{position:absolute;left:655px;top:2270px;list-style:none}
.bullets li{position:relative;padding-left:21px;height:37px;font-size:16px;color:var(--muted)}
.bullets li::before{content:"";position:absolute;left:0;top:6px;width:11px;height:11px;border-radius:50%;background:var(--navy)}

/* testimonials */
.testi{position:absolute;left:0;top:2533px;width:1200px;height:322px;background:linear-gradient(180deg,#5b8cbe,#4d7dae)}
.testi-title{color:var(--white)}
.quote-mark{position:absolute;left:0;width:1200px;text-align:center;top:2620px;font-size:58px;font-weight:800;font-style:italic;color:var(--white);line-height:1}
.testi-text{position:absolute;left:190px;top:2668px;width:820px;text-align:center;color:var(--white);font-size:16px;line-height:19px}
.testi-name{position:absolute;left:0;width:1200px;text-align:center;top:2742px;color:var(--white);font-size:15px;font-weight:700;font-style:italic}
.avatar{position:absolute;left:547px;top:2786px;width:106px;height:106px;border-radius:50%;border:4px solid var(--red);background:radial-gradient(circle at 50% 40%,#8a6a55,#2b3c5a)}

/* projects */
.tile-caption{position:absolute;color:var(--white);z-index:2}

/* footer */
.footer{position:absolute;left:0;top:3760px;width:1200px;height:417px;background:var(--footer)}
.f-head{position:absolute;top:3850px;color:var(--white);font-size:15.5px;font-weight:700;letter-spacing:.3px}
.f-item{position:absolute;color:var(--white);font-size:14.5px;line-height:18px}
.f-input{position:absolute;left:874px;top:3955px;width:188px;height:31px;border:1px solid #9fb4cf;color:#c9d5e4;font-size:12.5px;padding:7px 20px}
.f-submit{position:absolute;left:872px;top:3997px;width:98px;height:28px;background:var(--red);color:var(--white);font-weight:700;font-size:15px;display:flex;align-items:center;justify-content:center}
.bottom-bar{position:absolute;left:0;top:4096px;width:1200px;height:81px;background:var(--footer-deep)}
.social{position:absolute;top:4112px;width:18px;height:18px;border:2px solid var(--white);border-radius:50%}
</style>
</head>
<body>
<div class="page">

  <header class="header">
    <div class="brand"><span>Hartwell Painting</span><span class="brand-dot"></span></div>
    <nav class="nav">
      <a class="active" style="left:547px">HOME</a>
      <a style="left:645px">ABOUT US</a>
      <a style="left:775px">SERVICES</a>
      <a style="left:897px">PROJECTS</a>
      <a class="contact-btn">CONTACT</a>
    </nav>
  </header>

  <section class="hero">
    <div class="photo" role="img" aria-label="Paint roller resting on an open paint can" style="left:690px;top:130px;width:400px;height:540px;background:radial-gradient(ellipse at 45% 60%,#1a5db0 0%,#0c4a96 55%,rgba(11,74,150,0) 75%)"></div>
    <div class="hero-kicker">We Make Your Home</div>
    <h1 class="hero-word">Colorful</h1>
    <div class="hero-stroke"></div>
    <div class="arrow-ring" style="left:89px;top:347px"></div>
    <svg class="abs" style="left:108px;top:364px;z-index:2" width="24" height="28"><polyline points="18,2 6,14 18,26" fill="none" stroke="#fff" stroke-width="3"/></svg>
    <div class="arrow-ring" style="left:1051px;top:347px"></div>
    <svg class="abs" style="left:1072px;top:364px;z-index:2" width="24" height="28"><polyline points="6,2 18,14 6,26" fill="none" stroke="#fff" stroke-width="3"/></svg>
    <div class="dots" style="left:569px;top:585px"><span class="on"></span><span></span><span></span></div>
  </section>
  <svg class="abs" style="left:0;top:680px" width="1200" height="90" viewBox="0 0 1200 90">
    <path d="M0 30 L60 22 L110 34 L180 18 L240 30 L300 20 L380 34 L450 24 L520 36 L600 28 L680 38 L760 26 L840 36 L920 24 L1000 34 L1080 22 L1140 32 L1200 20 L1200 90 L0 90 Z" fill="#fff"/>
    <path d="M0 44 L90 38 L200 48 L320 40 L460 50 L600 44 L760 52 L900 42 L1040 50 L1200 40" fill="none" stroke="#d8e4f2" stroke-width="6" opacity=".7"/>
  </svg>

  <section>
    <h2 class="title" style="left:175px;top:860px">About Us</h2>
    <div class="rule" style="left:175px;top:900px;width:100px"></div>
    <p class="body abs" style="left:174px;top:932px;width:374px">We are family owned and operated with over 10 years’ experience. We pride our self in performing to the highest degree of workmanship standards. Hartwell Painting is your best choice for commercial, residential and multi-family painting in the DFW/-Forth Worth area.</p>
    <div class="btn" style="left:175px;top:1075px;width:117px;height:36px">Read More</div>
    <div class="photo" role="img" aria-label="Smiling painter in blue overalls giving a thumbs up next to a paint roller" style="left:608px;top:819px;width:527px;height:381px;background:radial-gradient(ellipse at 50% 55%,#dfeaf5 0%,#f1f6fb 60%,#ffffff 80%)"></div>
  </section>

  <section>
    <div class="services-bg"></div>
    <svg class="abs" style="left:0;top:1230px" width="1200" height="40" viewBox="0 0 1200 40">
      <path d="M0 22 L100 14 L220 24 L360 12 L500 22 L660 10 L820 22 L980 12 L1100 22 L1200 14 L1200 40 L0 40 Z" fill="#eef5fc"/>
    </svg>
    <h2 class="title center" style="top:1315px">Our Services</h2>
    <div class="rule center-rule" style="top:1357px"></div>

    <div class="svc-circle photo" role="img" aria-label="Blue painted living room wall with framed artwork above a dresser" style="left:150px;top:1441px;background:linear-gradient(160deg,#1f5fa5,#0f3f78 60%,#8a6a4e)"></div>
    <div class="svc-circle photo" role="img" aria-label="Two workers painting a commercial wall" style="left:471px;top:1441px;border:4px solid var(--red);background:linear-gradient(170deg,#6fa24a,#7b8c99 55%,#2c5f8f)"></div>
    <div class="svc-circle photo" role="img" aria-label="Painter on a ladder rolling paint onto an interior wall" style="left:794px;top:1441px;background:linear-gradient(160deg,#e8edf3,#c9d3de 60%,#8aa3bf)"></div>

    <svg class="abs" style="left:86px;top:1632px" width="26" height="54"><polyline points="24,2 2,27 24,52" fill="none" stroke="#333" stroke-width="2.5"/></svg>
    <svg class="abs" style="left:1084px;top:1632px" width="26" height="54"><polyline points="2,2 24,27 2,52" fill="none" stroke="#333" stroke-width="2.5"/></svg>

    <h3 class="svc-name" style="left:128px;top:1729px">Residental Painting</h3>
    <h3 class="svc-name" style="left:450px;top:1729px">Commercial Painting</h3>
    <h3 class="svc-name" style="left:771px;top:1731px">Multi - House Painting</h3>

    <p class="body svc-text" style="left:163px;top:1772px">We simply dummy text of the printing and typesetting industry. Lorem Ipsum has been the indus-try’s standard dummy text ever the industry’s since the</p>
    <p class="body svc-text" style="left:472px;top:1772px">We simply dummy text of the printing and typesetting industry. Lorem Ipsum has been the indus-try’s standard dummy text ever the industry’s since the</p>
    <p class="body svc-text" style="left:794px;top:1772px">We simply dummy text of the printing and typesetting industry. Lorem Ipsum has been the indus-try’s standard dummy text ever the industry’s since the</p>

    <div class="btn" style="left:546px;top:1889px;width:104px;height:36px">View</div>
    <div class="dots svc-dots" style="left:569px;top:1980px"><span class="on"></span><span></span><span></span></div>
  </section>

  <section>
    <div class="photo" role="img" aria-label="Painter in blue cap and overalls holding a roller in front of a bright blue paint swatch" style="left:113px;top:2108px;width:447px;height:389px;background:linear-gradient(100deg,#ffffff 10%,#3fa4dc 45%,#1f8fd0 75%,#ffffff 100%)"></div>
    <h2 class="title" style="left:649px;top:2105px">Why Choose Us?</h2>
    <div class="rule" style="left:649px;top:2143px;width:100px"></div>
    <p class="body abs" style="left:647px;top:2173px;width:373px">We are family owned and operated with over 10 years’ experience. We pride our self in performing to the highest degree of workmanship standards. Hartwell Painting</p>
    <ul class="bullets">
      <li>Water Proofing</li>
      <li>Color Proof</li>
      <li>Window Washing</li>
    </ul>
    <div class="btn" style="left:649px;top:2395px;width:116px;height:34px">Read More</div>
  </section>

  <section>
    <div class="testi photo" role="img" aria-label="Paint cans, brushes and a ladder on a drop cloth behind a blue overlay"></div>
    <svg class="abs" style="left:0;top:2520px" width="1200" height="30" viewBox="0 0 1200 30">
      <path d="M0 0 L1200 0 L1200 14 L1100 20 L980 12 L840 22 L700 12 L560 20 L420 10 L280 22 L140 12 L0 18 Z" fill="#fff"/>
    </svg>
    <svg class="abs" style="left:0;top:2838px" width="1200" height="30" viewBox="0 0 1200 30">
      <path d="M0 14 L120 8 L260 18 L400 6 L540 16 L700 8 L860 18 L1000 8 L1200 16 L1200 30 L0 30 Z" fill="#fff"/>
    </svg>
    <h2 class="title center testi-title" style="top:2574px">Testimonials</h2>
    <div class="rule center-rule" style="top:2613px"></div>
    <div class="quote-mark">“</div>
    <p class="testi-text">We are satisfied  is simply dummy text of the printing and typesetting industry. Lorem Ipsum has been the indus-try’s standard dummy text ever since the 1500s, when an unknown printer took a galley of type and scrambled it to make specimen book.</p>
    <div class="testi-name">- DANA RUELLE</div>
    <svg class="abs" style="left:86px;top:2670px" width="26" height="54"><polyline points="24,2 2,27 24,52" fill="none" stroke="#fff" stroke-width="2.5"/></svg>
    <svg class="abs" style="left:1084px;top:2670px" width="26" height="54"><polyline points="2,2 24,27 2,52" fill="none" stroke="#fff" stroke-width="2.5"/></svg>
    <div class="avatar" role="img" aria-label="Client portrait"></div>
  </section>

  <section>
    <h2 class="title center" style="top:2942px">Our Projects</h2>
    <div class="rule center-rule" style="top:2983px"></div>

    <div class="photo" role="img" aria-label="Single-storey brick house exterior" style="left:156px;top:3049px;width:290px;height:194px;background:linear-gradient(180deg,#7fa9d6 0%,#9fbfe0 40%,#5b4b3e 60%,#6b7a4a 100%)"></div>
    <div class="photo" role="img" aria-label="Double-height interior lobby with tall windows" style="left:156px;top:3251px;width:290px;height:356px;background:linear-gradient(180deg,#5a5a5c,#3b3a3a 55%,#6a6d70)"></div>
    <div class="abs" style="left:156px;top:3251px;width:290px;height:356px;background:rgba(0,0,0,.18)"></div>
    <div class="tile-caption" style="left:283px;top:3412px;font-size:16px;text-decoration:underline">view</div>
    <div class="tile-caption" style="left:183px;top:3550px;font-size:16px;font-weight:700">Residental Painting</div>
    <div class="tile-caption" style="left:183px;top:3573px;font-size:14px">Chicago</div>

    <div class="photo" role="img" aria-label="White kitchen with island and pendant lights" style="left:454px;top:3044px;width:290px;height:280px;background:linear-gradient(180deg,#d9dcdf,#eceeef 50%,#a9a29a)"></div>
    <div class="photo" role="img" aria-label="Fitness studio interior with graphic wall panels" style="left:454px;top:3329px;width:290px;height:278px;background:linear-gradient(180deg,#3a3d44,#4b5a7a 40%,#6b6e72)"></div>

    <div class="photo" role="img" aria-label="Office wall clad in reclaimed wood boards" style="left:751px;top:3049px;width:290px;height:353px;background:linear-gradient(90deg,#7b8088 0%,#8e9299 45%,#6a5442 60%,#8a6a4e 100%)"></div>
    <div class="photo" role="img" aria-label="Stucco house exterior under blue sky" style="left:751px;top:3410px;width:290px;height:197px;background:linear-gradient(180deg,#2f6fc6 0%,#5b93d8 45%,#b8a895 65%,#7a8a5a 100%)"></div>

    <div class="btn" style="left:542px;top:3650px;width:116px;height:36px">View All</div>
  </section>

  <footer>
    <svg class="abs" style="left:0;top:3715px" width="1200" height="70" viewBox="0 0 1200 70">
      <path d="M0 30 L80 18 L160 34 L260 20 L360 36 L470 22 L580 34 L700 18 L820 32 L940 20 L1060 34 L1200 22 L1200 70 L0 70 Z" fill="#0b2a4e"/>
      <path d="M0 26 L140 20 L300 30 L480 18 L660 28 L860 16 L1040 28 L1200 18" fill="none" stroke="#1f4a7c" stroke-width="5" opacity=".8"/>
    </svg>
    <div class="footer"></div>

    <div class="f-head" style="left:151px">GET IN TOUCH</div>
    <div class="f-head" style="left:480px">MENUS</div>
    <div class="f-head" style="left:678px">USEFUL LINKS</div>
    <div class="f-head" style="left:874px">NEWSLETTER</div>

    <svg class="abs" style="left:151px;top:3893px" width="16" height="16" viewBox="0 0 24 24"><path d="M6.6 10.8a15 15 0 006.6 6.6l2.2-2.2a1 1 0 011-.25 11.4 11.4 0 003.6.6 1 1 0 011 1V20a1 1 0 01-1 1A17 17 0 013 4a1 1 0 011-1h3.5a1 1 0 011 1c0 1.25.2 2.45.6 3.6a1 1 0 01-.25 1z" fill="#fff"/></svg>
    <div class="f-item" style="left:177px;top:3900px;font-weight:700;font-size:16px">555-013-2847</div>
    <svg class="abs" style="left:151px;top:3933px" width="16" height="12" viewBox="0 0 16 12"><rect x=".5" y=".5" width="15" height="11" fill="#fff"/><polyline points="1,1 8,7 15,1" fill="none" stroke="#0b2a4e" stroke-width="1.4"/></svg>
    <div class="f-item" style="left:177px;top:3934px">info@hartwellpainting.com</div>
    <svg class="abs" style="left:152px;top:3962px" width="13" height="17" viewBox="0 0 12 16"><path d="M6 0a6 6 0 00-6 6c0 4.5 6 10 6 10s6-5.5 6-10a6 6 0 00-6-6zm0 8.3A2.3 2.3 0 118 6a2.3 2.3 0 01-2 2.3z" fill="#fff"/></svg>
    <div class="f-item" style="left:177px;top:3968px;width:200px">Address ipsum, address of place street.</div>

    <div class="f-item" style="left:481px;top:3900px">Home</div>
    <div class="f-item" style="left:481px;top:3934px">About Us</div>
    <div class="f-item" style="left:481px;top:3968px">Services</div>
    <div class="f-item" style="left:481px;top:4002px">Blogs &amp; News</div>
    <div class="f-item" style="left:481px;top:4036px">Contact</div>

    <div class="f-item" style="left:677px;top:3900px">Privacy Policy</div>
    <div class="f-item" style="left:677px;top:3934px">Terms &amp; Conditions</div>
    <div class="f-item" style="left:677px;top:3968px">Legal Informations</div>
    <div class="f-item" style="left:677px;top:4002px">Copyrights</div>

    <div class="f-item" style="left:874px;top:3900px;width:190px">Subscribe to out newsletter to get our latestupdates</div>
    <div class="f-input">Enter e- Mail id</div>
    <div class="f-submit">SUBMIT</div>

    <div class="bottom-bar"></div>
    <div class="f-item" style="left:153px;top:4112px">© 2020 Hartwellpainting. All rights reserved.</div>
    <div class="social" style="left:887px"></div>
    <div class="social" style="left:926px"></div>
    <div class="social" style="left:965px"></div>
    <div class="social" style="left:1004px"></div>
  </footer>

</div>
</body>
</html>
```